KVR Biz Cards

We are a property management company that manages luxury level residential estates. As such, we need a business card design that gives a high end feel. The idea at the moment is to list the services offered on the back of the card, and our company information on the front of the card.

Services for the back of the card are as follows:
Professional Property Management service, Home Hosting & Concierge Service, Holliday Home / Income Property Management

```html
<!DOCTYPE html>
<html lang="en">
<head>
<meta charset="utf-8">
<title>KVR Business Cards</title>
<link rel="stylesheet" href="https://fonts.googleapis.com/css2?family=Montserrat:wght@600&family=Questrial&family=Roboto:wght@400;500&display=swap">
<style>
  :root {
    --bronze: #8b5e34;
    --ink: #111111;
    --text: #2b2b2b;
    --paper: #ffffff;
    --backdrop: #e4e4e4;
  }
  html, body {
    margin: 0;
    width: 1200px;
    height: 1200px;
    overflow: hidden;
    background: var(--backdrop);
  }
  .card {
    position: absolute;
    left: 189px;
    width: 830px;
    height: 474px;
    background: var(--paper);
    border-radius: 28px;
    box-shadow: 0 8px 16px rgba(0,0,0,0.22);
    overflow: hidden;
  }
  .card--front { top: 100px; }
  .card--back { top: 634px; }
  .centered {
    position: absolute;
    left: 0;
    width: 100%;
    text-align: center;
    margin: 0;
    white-space: nowrap;
  }
  .monogram {
    font-family: "Montserrat", sans-serif;
    font-weight: 600;
    color: var(--bronze);
    letter-spacing: 4px;
    line-height: 1;
  }
  .card--front .monogram { top: 133px; font-size: 62px; }
  .card--back .monogram { top: 130px; font-size: 46px; }
  .company {
    font-family: "Montserrat", sans-serif;
    font-weight: 600;
    color: var(--ink);
    letter-spacing: 0.5px;
    line-height: 1;
  }
  .card--front .company { top: 205px; font-size: 31px; }
  .card--back .company { top: 188px; font-size: 24px; }
  .tagline {
    font-family: "Questrial", sans-serif;
    color: var(--bronze);
    letter-spacing: 0.8px;
    line-height: 1;
  }
  .card--front .tagline { top: 236px; font-size: 20px; }
  .card--back .tagline { top: 211px; font-size: 15px; }
  .person {
    position: absolute;
    right: 418px;
    top: 300px;
    text-align: right;
    font-family: "Roboto", sans-serif;
  }
  .person__name {
    margin: 0;
    font-size: 42px;
    font-weight: 500;
    color: var(--bronze);
    line-height: 1;
  }
  .person__role {
    margin: 8px 0 0;
    font-size: 19px;
    color: var(--text);
  }
  .divider {
    position: absolute;
    left: 428px;
    top: 296px;
    width: 2px;
    height: 81px;
    background: var(--bronze);
  }
  .contacts {
    position: absolute;
    left: 445px;
    top: 292px;
    margin: 0;
    padding: 0;
    list-style: none;
    font-family: "Roboto", sans-serif;
    font-size: 19px;
    color: var(--text);
  }
  .contacts li {
    display: flex;
    align-items: center;
    gap: 5px;
    height: 31px;
  }
  .contacts svg { width: 18px; height: 18px; fill: var(--bronze); }
  .address-band {
    position: absolute;
    left: 0;
    top: 411px;
    width: 100%;
    height: 29px;
    background: var(--bronze);
    color: var(--paper);
    font-family: "Roboto", sans-serif;
    font-size: 18px;
    line-height: 29px;
    text-align: center;
  }
  .services__headline {
    top: 277px;
    font-family: "Roboto", sans-serif;
    font-weight: 500;
    font-size: 35px;
    color: var(--bronze);
  }
  .services__list {
    top: 354px;
    font-family: "Roboto", sans-serif;
    font-size: 19px;
    line-height: 31px;
    color: var(--text);
  }
</style>
</head>
<body>
  <section class="card card--front">
    <p class="centered monogram">KVR</p>
    <p class="centered company">VERIDALE MANAGEMENT</p>
    <p class="centered tagline">Crafted to Keep Your Estate at Ease</p>

    <div class="person">
      <p class="person__name">ADRIAN COLE</p>
      <p class="person__role">Managing Director</p>
    </div>
    <div class="divider"></div>
    <ul class="contacts">
      <li>
        <svg viewBox="0 0 24 24" aria-hidden="true"><path d="M6.6 10.8a15.1 15.1 0 0 0 6.6 6.6l2.2-2.2a1 1 0 0 1 1-.25 11.4 11.4 0 0 0 3.6.57 1 1 0 0 1 1 1V20a1 1 0 0 1-1 1A17 17 0 0 1 3 4a1 1 0 0 1 1-1h3.5a1 1 0 0 1 1 1c0 1.25.2 2.45.57 3.57a1 1 0 0 1-.25 1z"/></svg>
        555 014 2786
      </li>
      <li>
        <svg viewBox="0 0 24 24" aria-hidden="true"><path d="M2 5h20v2l-10 6L2 7z"/><path d="M2 9l10 6 10-6v10H2z"/></svg>
        info@veridalemgmt.com
      </li>
      <li>
        <svg viewBox="0 0 24 24" aria-hidden="true"><circle cx="12" cy="12" r="10"/></svg>
        www.veridalemgmt.com
      </li>
    </ul>
    <div class="address-band">1840 Marina Crest Way Seabrook CA 92100</div>
  </section>

  <section class="card card--back">
    <p class="centered monogram">KVR</p>
    <p class="centered company">VERIDALE MANAGEMENT</p>
    <p class="centered tagline">Crafted to Keep Your Estate at Ease</p>
    <h2 class="centered services__headline">Professional Property Management service</h2>
    <p class="centered services__list">Home Hosting &amp; Concierge Service,<br>Holliday Home / Income Property Management</p>
  </section>
</body>
</html>
```